Honeyvale Stitchery Needs a Beautiful Website

I need a new website for this new E-commerce. I sell handmade baby crochets, e.g. booties, headbands, hats, etc. I need a feminine and soft design to make the moms-to-be say 'oohh ahh'. I'd like pink, blue and gray. I'd like an inviting homepage, and nice regular pages where people can see and order the products.

Industry/Entity Type

Baby

Requirements
Must have
• beautiful, soft, feminine design. Please use pictures of the colors I'd like: brown, yellow, pink and blue. Any combination, but definitely include brown.

```html
<!DOCTYPE html>
<html lang="en">
<head>
<meta charset="utf-8">
<title>Honeyvale Stitchery</title>
<link href="https://fonts.googleapis.com/css2?family=Open+Sans:wght@400;600;700&display=swap" rel="stylesheet">
<style>
:root{
  --pink:#ff4f86;
  --pink-soft:#fde8ee;
  --cyan:#1ec4e0;
  --cyan-dark:#0fb2cf;
  --navy:#3a4670;
  --ink:#3d4a6b;
  --line:#e6e6e6;
  --page:#f1f1f1;
  --foot:#e3f5fb;
  --crown-pink:#ee2f72;
  --crown-blue:#5fd0e6;
  --shoe-navy:#3b4874;
  --shoe-black:#2a2a2a;
  --shoe-brown:#6b5f58;
}
*{margin:0;padding:0;box-sizing:border-box}
html,body{width:778px;height:1200px;overflow:hidden}
body{font-family:"Open Sans",sans-serif;background:var(--page);position:relative;color:#555}
.abs{position:absolute}
.top-band{left:0;top:0;width:778px;height:92px;background:var(--pink-soft);border-top:3px solid #cdeef6}
.brand{left:53px;top:34px;display:flex;align-items:center;gap:7px}
.brand-dot{width:16px;height:16px;border-radius:50%;background:var(--pink)}
.brand-name{font-size:21px;font-weight:700;color:var(--pink)}
.locale{top:14px;font-size:7px;color:#666}
.delivery{left:470px;top:33px;text-align:right;width:116px;color:#7a7a7a;line-height:1.1}
.delivery b{display:block;font-size:11px;font-weight:600}
.delivery span{font-size:14px;color:#666}
.lock{left:604px;top:41px}
.cart{left:630px;top:32px;width:83px;height:32px;border:1px solid #ddd;border-radius:3px;background:#f3f3f3;display:flex}
.cart-icon{width:32px;height:32px;background:var(--pink);border-radius:3px;display:flex;align-items:center;justify-content:center}
.cart-text{padding:5px 0 0 6px;font-size:7px;color:#666;line-height:1.5}
.cart-text em{font-style:normal;color:#aaa}
.sheet{left:51px;top:92px;width:676px;height:895px;background:#fff}
.nav{left:65px;top:105px;width:648px;height:32px;background:var(--navy);border-radius:3px;display:flex;align-items:center;padding-left:21px}
.nav a{font-size:8px;color:#fff;text-decoration:none;margin-right:38px}
.nav a.active{color:var(--pink)}
.search{left:588px;top:112px;width:117px;height:18px;background:#5a6690;border-radius:3px}
.search svg{position:absolute;left:6px;top:4px}
.side-head{left:65px;width:149px;height:29px;background:linear-gradient(var(--cyan),var(--cyan-dark));color:#fff;font-size:10px;font-weight:700;padding:8px 15px}
.cats{left:65px;top:192px;width:149px;list-style:none}
.cats li{height:19.4px;border-bottom:1px solid #eee;background:linear-gradient(#fff,#f3f3f3);font-size:6px;color:#888;padding:6px 0 0 21px;position:relative;text-transform:uppercase}
.cats li::before{content:"";position:absolute;left:11px;top:8px;border:2px solid transparent;border-left:3px solid #bbb}
.cats li .plus{position:absolute;right:6px;top:6px;width:7px;height:7px;border-radius:50%;background:#999}
.special{left:65px;top:471px;width:149px;height:133px;border:1px solid var(--line)}
.special-img{position:absolute;left:12px;top:16px;width:60px;height:60px;border-radius:4px;background:linear-gradient(160deg,#4a4a4a,var(--shoe-black) 60%,#dcdcdc)}
.special-info{position:absolute;left:81px;top:24px;font-size:6px;color:#888;line-height:1.4}
.special-info .price{font-size:11px;color:#333}
.special-info .old{font-size:10px;color:#bbb;text-decoration:line-through}
.btn-small{position:absolute;left:12px;top:103px;background:var(--cyan);color:#fff;font-size:6px;padding:5px 10px;border-radius:2px}
.sale{left:65px;top:621px;width:149px;height:171px;background:linear-gradient(#ff6f9a,#ff4d7f);border-radius:3px;color:#fff;text-align:center;padding-top:14px}
.sale h3{font-size:30px;font-weight:700;line-height:1}
.sale .tiny{font-size:6px;font-weight:700;line-height:1.3}
.sale .mid{font-size:10px;font-weight:700;margin-top:2px;line-height:1.2}
.sale .big{font-size:21px;font-weight:700;line-height:1.15}
.sale .btn{display:inline-block;background:#fff;color:#666;font-size:8px;font-weight:600;padding:6px 10px;margin-top:12px;border-radius:2px}
.hero{left:231px;top:154px;width:482px;height:220px;border:1px solid #eee;background:linear-gradient(#fff,#f4f4f6);overflow:hidden}
.hero-img{position:absolute;left:150px;top:0;width:332px;height:220px;background:linear-gradient(100deg,rgba(255,255,255,0) 0%,#6cc3ee 22%,#2b95dc 50%,#8fdc48 78%,#e9f5e0 100%)}
.hero-copy{position:absolute;left:57px;top:38px;color:var(--ink)}
.hero-copy h2{font-size:39px;font-weight:400;line-height:.95}
.hero-copy h3{font-size:21px;font-weight:400;line-height:1.05}
.hero-copy p{font-size:6px;margin-top:12px;line-height:1.7;width:140px}
.hero-copy .from{font-size:12px;margin-top:6px}
.hero-copy .from b{font-size:16px;font-weight:600}
.hero-copy .btn{display:inline-block;background:var(--cyan);color:#fff;font-size:8px;font-weight:700;padding:6px 10px;margin-top:6px}
.promo{top:386px;width:151px;height:114px;border:1px solid;border-radius:3px;background:linear-gradient(#fff,#f6f6f6);overflow:hidden}
.promo h4{position:absolute;left:18px;top:32px;font-size:19px;font-weight:400;color:#444;line-height:1;z-index:1}
.promo small{display:block;font-size:11px;color:#aaa}
.promo .shop{position:absolute;left:18px;top:90px;font-size:6px;font-weight:700}
.promo .pic{position:absolute;right:8px;top:16px;width:74px;height:86px;border-radius:6px}
.feat-head{left:231px;top:512px;width:482px;height:29px;background:linear-gradient(var(--cyan),var(--cyan-dark));color:#fff;font-size:10px;font-weight:700;padding:8px 15px}
.card{width:151px;height:198px;border:1px solid var(--line)}
.card .pic{position:absolute;left:6px;top:6px;width:139px;height:127px;border-radius:4px}
.card .foot{position:absolute;left:0;top:137px;width:149px;height:59px;background:linear-gradient(#fff,#f3f3f3)}
.card .name{position:absolute;left:10px;top:15px;font-size:6px;color:#888;text-transform:uppercase}
.card .price{position:absolute;left:10px;top:32px;font-size:10px;color:var(--pink)}
.card .price s{color:#999}
.card .btns{position:absolute;right:9px;top:12px;display:flex;gap:4px}
.card .btns span{width:20px;height:20px;border-radius:3px;display:flex;align-items:center;justify-content:center}
.info-btn{background:#8ed9ea}
.cart-btn{background:var(--cyan)}
.pink-crown{background:linear-gradient(170deg,#fbe4ec,var(--crown-pink) 45%,#c91f5c 70%,#f7f7f7)}
.blue-crown{background:linear-gradient(170deg,#e6f7fb,var(--crown-blue) 45%,#33b6d3 70%,#f7f7f7)}
.navy-shoe{background:linear-gradient(160deg,#eef0f6,var(--shoe-navy) 45%,#2a3457 70%,#eeeeee)}
.black-shoe{background:linear-gradient(160deg,#ececec,var(--shoe-black) 45%,#151515 70%,#eeeeee)}
.brown-shoe{background:linear-gradient(160deg,#efebe8,var(--shoe-brown) 45%,#4c433e 70%,#eeeeee)}
.footer{left:51px;top:987px;width:676px;height:154px;background:var(--foot)}
.fcol{position:absolute;top:27px;font-size:6.5px;color:#555;line-height:2.1}
.fcol h5{font-size:6.5px;font-weight:600;color:#777;margin-bottom:8px;line-height:1}
.fcol .sq{display:inline-block;width:5px;height:5px;background:#555;margin-right:6px}
.fcol .phone{font-size:14px;color:#555;display:flex;align-items:center;gap:8px;margin-top:6px}
.bottom-bar{left:51px;top:1141px;width:676px;height:28px;background:linear-gradient(#2cc9e3,#16b4d0);color:#fff;font-size:5.5px;padding:10px 14px}
</style>
</head>
<body>
<div class="abs top-band"></div>
<div class="abs brand"><span class="brand-dot"></span><span class="brand-name">Honeyvale Stitchery</span></div>
<div class="abs locale" style="left:673px">$ ▾</div>
<div class="abs locale" style="left:698px">En ▾</div>
<div class="abs delivery"><b>ORDER DELIVERY:</b><span>+000-0000-0000</span></div>
<svg class="abs lock" width="12" height="15" viewBox="0 0 12 15"><path d="M3 7V4.5a3 3 0 0 1 6 0V7" fill="none" stroke="#888" stroke-width="1.6"/><rect x="1" y="7" width="10" height="8" rx="1" fill="#888"/></svg>
<div class="abs cart"><div class="cart-icon"><svg width="16" height="14" viewBox="0 0 16 14"><path d="M0 1h3l2 8h8l2-6H4" fill="none" stroke="#fff" stroke-width="1.8"/><circle cx="6" cy="12" r="1.4" fill="#fff"/><circle cx="12" cy="12" r="1.4" fill="#fff"/></svg></div><div class="cart-text">Cart<br><em>EMPTY</em></div></div>

<div class="abs sheet"></div>
<nav class="abs nav"><a class="active">HOME</a><a>SITEMAP</a><a>CONTACT</a></nav>
<div class="abs search"><svg width="10" height="10" viewBox="0 0 10 10"><circle cx="4" cy="4" r="3" fill="none" stroke="#fff" stroke-width="1.5"/><path d="M6.2 6.2L9 9" stroke="#fff" stroke-width="1.7"/></svg></div>

<div class="abs side-head" style="top:154px">CATEGORIES</div>
<ul class="abs cats">
  <li>Sets</li><li>One piece<span class="plus"></span></li><li>Handmade baby crochets</li><li>Bodysuits</li><li>Tops</li><li>Bottoms</li><li>Hats</li><li>Pajamas</li><li>Costumes</li><li>Headbands</li><li>Booties</li>
</ul>
<div class="abs side-head" style="top:425px">SPECIALS</div>
<div class="abs special">
  <div class="special-img" role="img" aria-label="Black crocheted baby booties with white laces"></div>
  <div class="special-info">ORGANIC OCEAN<br>WAVES DRESS<br><span class="price">$394.64</span><br>(-8%)<br><span class="old">$428.96</span></div>
  <span class="btn-small">All specials</span>
</div>
<div class="abs sale">
  <h3>SALE</h3>
  <div class="tiny">EXTRA LINES JUST ADDED</div>
  <div class="mid">UP TO</div>
  <div class="big">20% OFF</div>
  <div class="tiny" style="font-size:5px">PLUS FREE DELIVERY ON ORDERS<br>OVER $900</div>
  <span class="btn">SHOP NOW</span>
</div>

<div class="abs hero">
  <div class="hero-img" role="img" aria-label="Blue polka-dot baby sneakers with green laces"></div>
  <div class="hero-copy">
    <h2>NEW</h2><h3>ARRIVALS</h3>
    <p>DONEC VITAE DIAM UT PURUS LUCTUS FELISIS NULLECTUS.</p>
    <div class="from">FROM <b>$49.99</b></div>
    <span class="btn">SHOP NOW</span>
  </div>
</div>

<div class="abs promo" style="left:231px;border-color:#f6d2b8">
  <h4>PINK<small>CROWN</small></h4><span class="shop" style="color:#f26b2a">SHOP NOW ›</span>
  <div class="pic pink-crown" role="img" aria-label="Pink crocheted baby crown"></div>
</div>
<div class="abs promo" style="left:397px;border-color:#f6c9d6">
  <h4>POLLY</h4><span class="shop" style="color:var(--pink)">SHOP NOW ›</span>
  <div class="pic brown-shoe" role="img" aria-label="Brown crocheted baby sneakers with pink star"></div>
</div>
<div class="abs promo" style="left:564px;border-color:#9fe0ee">
  <h4>NEW<small>BABY</small></h4><span class="shop" style="color:#444">SHOP NOW ›</span>
  <div class="pic navy-shoe" role="img" aria-label="Navy crocheted baby sneakers with red star"></div>
</div>

<div class="abs feat-head">FEATURED PRODUCTS</div>

<div class="abs card" style="left:231px;top:557px"><div class="pic pink-crown" role="img" aria-label="Pink crocheted baby crown"></div><div class="foot"><span class="name">Pink Crown</span><span class="price">$122.51 <s>$128.96</s></span><div class="btns"><span class="info-btn"><svg width="10" height="10" viewBox="0 0 10 10"><circle cx="5" cy="5" r="4.5" fill="#fff"/><rect x="4.3" y="4" width="1.4" height="4" fill="#8ed9ea"/><circle cx="5" cy="2.6" r=".8" fill="#8ed9ea"/></svg></span><span class="cart-btn"><svg width="11" height="10" viewBox="0 0 16 14"><path d="M0 1h3l2 8h8l2-6H4" fill="none" stroke="#fff" stroke-width="2"/><circle cx="6" cy="12" r="1.5" fill="#fff"/><circle cx="12" cy="12" r="1.5" fill="#fff"/></svg></span></div></div></div>
<div class="abs card" style="left:397px;top:557px"><div class="pic blue-crown" role="img" aria-label="Light blue crocheted baby crown"></div><div class="foot"><span class="name">Blue Crown</span><span class="price">$628.96</span><div class="btns"><span class="info-btn"><svg width="10" height="10" viewBox="0 0 10 10"><circle cx="5" cy="5" r="4.5" fill="#fff"/><rect x="4.3" y="4" width="1.4" height="4" fill="#8ed9ea"/><circle cx="5" cy="2.6" r=".8" fill="#8ed9ea"/></svg></span><span class="cart-btn"><svg width="11" height="10" viewBox="0 0 16 14"><path d="M0 1h3l2 8h8l2-6H4" fill="none" stroke="#fff" stroke-width="2"/><circle cx="6" cy="12" r="1.5" fill="#fff"/><circle cx="12" cy="12" r="1.5" fill="#fff"/></svg></span></div></div></div>
<div class="abs card" style="left:564px;top:557px"><div class="pic navy-shoe" role="img" aria-label="Navy crocheted baby sneakers with red star"></div><div class="foot"><span class="name">Starlet Blue</span><span class="price">$394.64 <s>$428.96</s></span><div class="btns"><span class="info-btn"><svg width="10" height="10" viewBox="0 0 10 10"><circle cx="5" cy="5" r="4.5" fill="#fff"/><rect x="4.3" y="4" width="1.4" height="4" fill="#8ed9ea"/><circle cx="5" cy="2.6" r=".8" fill="#8ed9ea"/></svg></span><span class="cart-btn"><svg width="11" height="10" viewBox="0 0 16 14"><path d="M0 1h3l2 8h8l2-6H4" fill="none" stroke="#fff" stroke-width="2"/><circle cx="6" cy="12" r="1.5" fill="#fff"/><circle cx="12" cy="12" r="1.5" fill="#fff"/></svg></span></div></div></div>

<div class="abs card" style="left:231px;top:772px"><div class="pic black-shoe" role="img" aria-label="Black crocheted baby sneakers with white laces"></div><div class="foot"><span class="name">Starlet Black</span><span class="price">$928.96</span><div class="btns"><span class="info-btn"><svg width="10" height="10" viewBox="0 0 10 10"><circle cx="5" cy="5" r="4.5" fill="#fff"/><rect x="4.3" y="4" width="1.4" height="4" fill="#8ed9ea"/><circle cx="5" cy="2.6" r=".8" fill="#8ed9ea"/></svg></span><span class="cart-btn"><svg width="11" height="10" viewBox="0 0 16 14"><path d="M0 1h3l2 8h8l2-6H4" fill="none" stroke="#fff" stroke-width="2"/><circle cx="6" cy="12" r="1.5" fill="#fff"/><circle cx="12" cy="12" r="1.5" fill="#fff"/></svg></span></div></div></div>
<div class="abs card" style="left:397px;top:772px"><div class="pic brown-shoe" role="img" aria-label="Brown crocheted baby sneakers with pink star"></div><div class="foot"><span class="name">Starlet</span><span class="price">$928.96</span><div class="btns"><span class="info-btn"><svg width="10" height="10" viewBox="0 0 10 10"><circle cx="5" cy="5" r="4.5" fill="#fff"/><rect x="4.3" y="4" width="1.4" height="4" fill="#8ed9ea"/><circle cx="5" cy="2.6" r=".8" fill="#8ed9ea"/></svg></span><span class="cart-btn"><svg width="11" height="10" viewBox="0 0 16 14"><path d="M0 1h3l2 8h8l2-6H4" fill="none" stroke="#fff" stroke-width="2"/><circle cx="6" cy="12" r="1.5" fill="#fff"/><circle cx="12" cy="12" r="1.5" fill="#fff"/></svg></span></div></div></div>
<div class="abs card" style="left:564px;top:772px"><div class="pic pink-crown" role="img" aria-label="Pink crocheted baby crown"></div><div class="foot"><span class="name">Pink Crown</span><span class="price">$428.96</span><div class="btns"><span class="info-btn"><svg width="10" height="10" viewBox="0 0 10 10"><circle cx="5" cy="5" r="4.5" fill="#fff"/><rect x="4.3" y="4" width="1.4" height="4" fill="#8ed9ea"/><circle cx="5" cy="2.6" r=".8" fill="#8ed9ea"/></svg></span><span class="cart-btn"><svg width="11" height="10" viewBox="0 0 16 14"><path d="M0 1h3l2 8h8l2-6H4" fill="none" stroke="#fff" stroke-width="2"/><circle cx="6" cy="12" r="1.5" fill="#fff"/><circle cx="12" cy="12" r="1.5" fill="#fff"/></svg></span></div></div></div>

<footer class="abs footer">
  <div class="fcol" style="left:14px"><h5>INFORMATION</h5>Specials<br>New products<br>Best sellers<br>Our stores<br>Contact us<br>Sitemap</div>
  <div class="fcol" style="left:180px"><h5>MY ACCOUNT</h5>My orders<br>My credit slips<br>My addresses<br>My personal info<br>My vouchers<br>My favorite products.<br>My loyalty points<br>Referral program</div>
  <div class="fcol" style="left:346px"><h5>FOLLOW US</h5><span class="sq"></span>Chirpline<br><span class="sq"></span>Friendsly<br><span class="sq"></span>RSS</div>
  <div class="fcol" style="left:513px;line-height:1.5"><h5>CONTACT US</h5><b style="font-weight:600">My Company</b><br>company address<br>E-mail: mail@honeyvale-shop.org
    <div class="phone"><svg width="12" height="12" viewBox="0 0 12 12"><rect width="12" height="12" rx="2" fill="#555"/><path d="M3.5 2.5c-.8.8-.6 2.8 1.5 4.9s4.1 2.3 4.9 1.5l-1.4-1.4-1 .6C6.6 7.6 4.4 5.4 3.9 4.5l.6-1z" fill="#fff"/></svg>+ 0(000) 000-0000</div>
  </div>
</footer>
<div class="abs bottom-bar">© 2014 Powered by Loomfield.net™</div>
</body>
</html>
```